Advertising company unique advertising platform

we need a logo design for a new company based in Australia Melbourne. We develop innovated advertising platform where consumer can use this platform to get regular discount, as business owner they can use this platform for free advertisement. Payment for this advertisement platform only payable every two weeks, when I generate revenue for their business

Industry/Entity Type

Advertising

Contact Information for Business Card

Dale Pruitt | Co-Founder |Managing Director
Suite 718 263 Harrowgate Row Melbourne Vic 3000

ABN 41 902 615 273
Tel: +61 0491 528 307 | Email: dale.pruitt@corvelaxtro.com

Font styles to use
Decorative
Script

Requirements
Must have
• Try few different design and some round corner business card
Should not have
• One round corner business card...try 4 different colour background not only black, make sure two side is designed. Be creative so imagine you are giving this to a client make sure has wow factor, if you can also try one design with engrave like all the logo, words look 3d feel
• The word Advertising Platform use attached file font

```html
<!DOCTYPE html>
<html lang="en">
<head>
<meta charset="utf-8">
<title>Allway Market – Business Card</title>
<link href="https://fonts.googleapis.com/css2?family=Open+Sans:wght@400;600;700&display=swap" rel="stylesheet">
<style>
  :root {
    --page-bg: #e9e7e4;
    --card-dark: #2a2a2a;
    --ink-light: #e8e8e8;
    --accent-orange: #e8552f;
    --accent-teal: #2fe0b2;
    --grad-center: #f2c24c;
    --grad-mid: #eb8a3a;
    --grad-edge: #e0452c;
    --white: #ffffff;
  }
  * { margin: 0; padding: 0; box-sizing: border-box; }
  html, body {
    width: 1200px; height: 960px; overflow: hidden;
    background: var(--page-bg);
    font-family: "Open Sans", Arial, sans-serif;
  }
  .canvas { position: relative; width: 1200px; height: 960px; }

  .card {
    position: absolute;
    width: 600px;
    border-radius: 22px;
    overflow: hidden;
  }
  .card-front {
    left: 314px; top: 113px; height: 344px;
    background: var(--card-dark);
  }
  .card-back {
    left: 311px; top: 472px; height: 342px;
    background: radial-gradient(ellipse 62% 75% at 52% 38%, var(--grad-center) 0%, var(--grad-mid) 55%, var(--grad-edge) 100%);
  }

  .brand {
    position: absolute;
    display: flex; align-items: center; gap: 12px;
  }
  .brand-dot { border-radius: 50%; flex: none; }
  .brand-name { font-weight: 700; white-space: nowrap; line-height: 1.2; }

  .card-front .brand { left: 30px; top: 92px; }
  .card-front .brand-dot { width: 30px; height: 30px; background: var(--accent-orange); }
  .card-front .brand-name { font-size: 34px; color: var(--accent-orange); }

  .company-details {
    position: absolute; left: 28px; top: 194px;
    color: var(--ink-light); font-size: 14.5px; line-height: 20px;
  }
  .company-details .gap { margin-top: 3px; }
  .contact-line { display: flex; align-items: center; gap: 8px; }
  .contact-line svg { width: 13px; height: 12px; fill: var(--accent-orange); flex: none; }

  .person {
    position: absolute; right: 28px; top: 205px;
    text-align: right; font-size: 16px; line-height: 22px; text-transform: uppercase;
  }
  .person-name { color: var(--accent-orange); font-weight: 700; }
  .person-role { color: var(--accent-teal); }

  .card-back .brand { left: 50%; top: 136px; transform: translateX(-50%); }
  .card-back .brand-dot { width: 34px; height: 34px; background: var(--white); }
  .card-back .brand-name { font-size: 40px; color: var(--white); }

  .website {
    position: absolute; left: 0; right: 0; top: 293px;
    text-align: center; color: var(--white);
    font-size: 13.5px; letter-spacing: 5px;
  }
</style>
</head>
<body>
<div class="canvas">
  <section class="card card-front">
    <div class="brand">
      <span class="brand-dot"></span>
      <span class="brand-name">Allway Market</span>
    </div>

    <div class="company-details">
      <p>Corvelaxtro</p>
      <p>ABN 41 902 615 273</p>
      <p class="gap">Suite 718 263 Harrowgate Row</p>
      <p>Melbourne Vic 3000</p>
      <p class="contact-line gap">
        <svg viewBox="0 0 13 12" aria-hidden="true"><path d="M1 4 Q6.5 0 12 4 L10.5 5.5 L9 4.5 L9 3.5 Q6.5 2.6 4 3.5 L4 4.5 L2.5 5.5 Z M3 6 L10 6 L11.5 11 L1.5 11 Z"/></svg>
        +61 0491 528 307
      </p>
      <p class="contact-line">
        <svg viewBox="0 0 13 12" aria-hidden="true"><path d="M0.5 2.5 L12.5 2.5 L6.5 6.5 Z M0.5 4 L6.5 8 L12.5 4 L12.5 10 L0.5 10 Z"/></svg>
        dale.pruitt@corvelaxtro.com
      </p>
    </div>

    <div class="person">
      <p class="person-name">Dale Pruitt</p>
      <p class="person-role">Co-Founder</p>
      <p class="person-role">Managing Director</p>
    </div>
  </section>

  <section class="card card-back">
    <div class="brand">
      <span class="brand-dot"></span>
      <span class="brand-name">Allway Market</span>
    </div>
    <p class="website">www.corvelaxtro.com</p>
  </section>
</div>
</body>
</html>
```